Local fast-growing company in the service sector

We are looking for a modern business card design, which should also appear on our letterheads

Target Market(s)

Private and industrial sectors

Contact Information for Business Card

Vorname Name
Lindkofer Str. 18
71468 Talbrunn
Tel.: 07163-418259-0
Name@kovaltec-pbz.de

Colors
9d9d9d
919191
aaaaaa

Requirements
Must have
• The logo (file) in silver

```html
<!DOCTYPE html>
<html lang="de">
<head>
<meta charset="utf-8">
<title>Business Card – Kovaltec</title>
<link href="https://fonts.googleapis.com/css2?family=Work+Sans:wght@400;500;700&display=swap" rel="stylesheet">
<style>
  :root {
    --page-bg: #e6e6e6;
    --card-grey: #a4a4a5;
    --band-black: #050505;
    --name-grey: #b9b9b9;
    --text-dark: #1a1a1a;
    --logo-white: #ffffff;
    --icon-grey: #3a3a3a;
  }
  html, body {
    margin: 0;
    width: 1200px;
    height: 801px;
    overflow: hidden;
    background: var(--page-bg);
    font-family: "Work Sans", Arial, sans-serif;
  }
  .business-card {
    position: absolute;
    left: 150px;
    top: 128px;
    width: 900px;
    height: 545px;
    background: var(--card-grey);
    box-shadow: 0 6px 18px rgba(0,0,0,0.18);
  }
  .name-band {
    position: absolute;
    left: 0;
    top: 80px;
    width: 440px;
    height: 104px;
    background: var(--band-black);
  }
  .person-name {
    position: absolute;
    left: 78px;
    top: 24px;
    margin: 0;
    font-size: 28px;
    font-weight: 400;
    letter-spacing: 0.5px;
    color: var(--name-grey);
  }
  .person-role {
    position: absolute;
    left: 88px;
    top: 62px;
    margin: 0;
    font-size: 15px;
    font-weight: 400;
    letter-spacing: 1px;
    color: var(--name-grey);
  }
  .brand {
    position: absolute;
    left: 462px;
    top: 62px;
    display: flex;
    align-items: center;
    gap: 18px;
  }
  .brand-square {
    width: 74px;
    height: 74px;
    background: var(--logo-white);
  }
  .brand-text { display: flex; flex-direction: column; }
  .brand-name {
    font-size: 46px;
    font-weight: 700;
    line-height: 1;
    color: var(--logo-white);
    letter-spacing: 1px;
  }
  .brand-web {
    margin-top: 4px;
    font-size: 22px;
    font-weight: 700;
    color: var(--logo-white);
  }
  .address {
    position: absolute;
    right: 60px;
    top: 320px;
    margin: 0;
    font-style: normal;
    font-size: 19px;
    line-height: 1.4;
    color: var(--text-dark);
  }
  .contact-list {
    position: absolute;
    left: 104px;
    top: 432px;
    margin: 0;
    padding: 0;
    list-style: none;
    font-size: 19px;
    line-height: 1.5;
    color: var(--text-dark);
  }
  .contact-list li { display: flex; align-items: center; gap: 14px; }
  .contact-icon { width: 14px; height: 14px; flex: none; }
</style>
</head>
<body>
  <section class="business-card">
    <div class="name-band">
      <h1 class="person-name">MAREK LINDNER</h1>
      <p class="person-role">DIRECTOR</p>
    </div>

    <div class="brand">
      <div class="brand-square"></div>
      <div class="brand-text">
        <span class="brand-name">KOVALTEC</span>
        <span class="brand-web">kovaltec-pbz.de</span>
      </div>
    </div>

    <address class="address">
      Lindkofer Str. 18<br>
      71468 Talbrunn
    </address>

    <ul class="contact-list">
      <li>
        <svg class="contact-icon" viewBox="0 0 24 24" aria-hidden="true">
          <path fill="var(--icon-grey)" d="M6.6 10.8a15.1 15.1 0 0 0 6.6 6.6l2.2-2.2a1 1 0 0 1 1-.25 11.4 11.4 0 0 0 3.6.57 1 1 0 0 1 1 1V20a1 1 0 0 1-1 1A17 17 0 0 1 3 4a1 1 0 0 1 1-1h3.5a1 1 0 0 1 1 1c0 1.25.2 2.45.57 3.6a1 1 0 0 1-.25 1z"/>
        </svg>
        <span>07163-418259-0</span>
      </li>
      <li>
        <svg class="contact-icon" viewBox="0 0 24 24" aria-hidden="true">
          <rect x="3" y="5" width="18" height="14" fill="none" stroke="var(--icon-grey)" stroke-width="2"/>
          <path d="M3 6l9 7 9-7" fill="none" stroke="var(--icon-grey)" stroke-width="2"/>
        </svg>
        <span>Name@kovaltec-pbz.de</span>
      </li>
    </ul>
  </section>
</body>
</html>
```